Business Card Design Project

We need a business card design for a new construction company called 'KORVA HOLDINGS PTY.LTD' We run a construction based company for high end market homes in melbourne, we want something that looks professional and eye catching.The card needs to have a strong design to it something modern as the company name explains "korva." The final design should communicate professionalism and a strong image to our customers on the quality of our work.
On the business card i need
Name: Marek Holtvay
Mob:0417295031
Email:korva.holdings@mailbrook.example
Domestic/Residential/Commercial

```html
<!DOCTYPE html>
<html lang="en">
<head>
<meta charset="utf-8">
<title>Korva Holdings – Business Card</title>
<link href="https://fonts.googleapis.com/css2?family=Open+Sans:wght@400;600;700&display=swap" rel="stylesheet">
<style>
  :root {
    --page-bg: #e9e7e4;
    --card-light: #ffffff;
    --card-dark: #231f20;
    --ink: #231f20;
    --accent: #e3262b;
    --paper-text: #ffffff;
  }
  html, body {
    margin: 0;
    padding: 0;
    width: 1200px;
    height: 900px;
    overflow: hidden;
    background: var(--page-bg);
    font-family: "Open Sans", Arial, sans-serif;
  }
  .canvas {
    position: relative;
    width: 1200px;
    height: 900px;
  }
  .card {
    position: absolute;
    top: 270px;
    width: 540px;
    height: 359px;
    box-sizing: border-box;
    box-shadow: 0 4px 14px rgba(0,0,0,0.18);
  }
  .card--front { left: 40px; background: var(--card-light); color: var(--ink); }
  .card--back  { left: 620px; background: var(--card-dark); color: var(--paper-text); }

  .wordmark {
    position: absolute;
    margin: 0;
    font-weight: 700;
    font-size: 86px;
    line-height: 1;
    letter-spacing: -1px;
    text-transform: lowercase;
  }
  .company-line {
    position: absolute;
    margin: 0;
    font-weight: 700;
    font-size: 13px;
    letter-spacing: 4.2px;
    color: var(--accent);
    white-space: nowrap;
  }
  .card--front .wordmark { right: 24px; top: 40px; color: var(--ink); }
  .card--front .company-line { right: 24px; top: 140px; }

  .card--back .wordmark { left: 0; right: 0; text-align: center; top: 112px; color: var(--paper-text); }
  .card--back .company-line { left: 0; right: 0; text-align: center; top: 212px; }

  .person-name {
    position: absolute;
    left: 24px;
    top: 212px;
    margin: 0;
    font-size: 20px;
    font-weight: 700;
    color: var(--accent);
  }
  .contact {
    position: absolute;
    left: 24px;
    top: 258px;
    margin: 0;
    font-size: 13px;
    line-height: 20px;
  }
  .contact dt { display: inline; font-weight: 700; }
  .contact dd { display: inline; margin: 0; }
  .contact div { margin: 0; }

  .services {
    position: absolute;
    margin: 0;
    padding: 0;
    list-style: none;
    display: flex;
    font-size: 18px;
    white-space: nowrap;
  }
  .services li + li {
    border-left: 1.5px solid var(--accent);
    margin-left: 5px;
    padding-left: 5px;
  }
  .card--front .services { right: 12px; top: 316px; color: var(--ink); }
  .card--back .services { left: 0; right: 0; justify-content: center; top: 278px; color: var(--paper-text); }
</style>
</head>
<body>
<main class="canvas">
  <section class="card card--front" aria-label="Business card front">
    <p class="wordmark">korva</p>
    <p class="company-line">KORVA HOLDINGS PTY.LTD</p>
    <h1 class="person-name">Marek Holtvay</h1>
    <dl class="contact">
      <div><dt>Mobile</dt> <dd>: 0417295031</dd></div>
      <div><dt>Email</dt> <dd>: korva.holdings@mailbrook.example</dd></div>
    </dl>
    <ul class="services">
      <li>Domestic</li>
      <li>Residential</li>
      <li>Commercial</li>
    </ul>
  </section>

  <section class="card card--back" aria-label="Business card back">
    <p class="wordmark">korva</p>
    <p class="company-line">KORVA HOLDINGS PTY.LTD</p>
    <ul class="services">
      <li>Domestic</li>
      <li>Residential</li>
      <li>Commercial</li>
    </ul>
  </section>
</main>
</body>
</html>
```